Business Card Design

We are an import/export consulting business dealing with all aspects of import/export regulations. Our current design if you look at our website (www.tavrelis.com) are different country flags. It is our business to stay up to date on laws and regulations. We assist companies worldwide. We would like to keep with the flag theme but something different or maybe someone can come up with something totally different that would capture our attention. We are open to suggestions. This design then will transfer over to letterhead, our website, marketing brochures, etc.

Industry/Entity Type

Marketing

Contact Information for Business Card

Dorothy M. Tavrelis, President
Tavrelis Global Advisors, LLC
7 Birchwood Lane,
Milford, VT 05712

```html
<!DOCTYPE html>
<html lang="en">
<head>
<meta charset="utf-8">
<title>Tavrelis Global Advisors – Business Card</title>
<link rel="stylesheet" href="https://fonts.googleapis.com/css2?family=Ubuntu:wght@400;500;700&display=swap">
<style>
  :root {
    --bg: #ecebe8;
    --red: #a61e22;
    --navy: #121a36;
    --gold: #d4a62a;
    --lime: #c9bf2a;
    --white: #ffffff;
    --paper: #f7f8fa;
    --ink: #1b2a4a;
  }
  * { box-sizing: border-box; margin: 0; padding: 0; }
  html, body { width: 1200px; height: 1000px; overflow: hidden; }
  body {
    background: var(--bg);
    font-family: "Ubuntu", sans-serif;
    position: relative;
  }
  .card {
    position: absolute;
    left: 290px;
    width: 620px;
    height: 354px;
    box-shadow: 0 6px 18px rgba(0,0,0,.18);
    overflow: hidden;
  }
  /* Front */
  .card-front { top: 100px; background: var(--red); padding: 18px; }
  .frame-navy { background: var(--navy); height: 100%; padding: 14px; }
  .frame-gold { background: var(--gold); height: 100%; padding: 11px; }
  .front-field {
    background: var(--white); height: 100%;
    display: flex; flex-direction: column; align-items: center; justify-content: center;
    gap: 26px;
  }
  .brand { display: flex; align-items: center; gap: 12px; }
  .brand-dot {
    width: 58px; height: 58px; border-radius: 50%;
    background: var(--navy); flex: none;
  }
  .brand-name {
    font-weight: 500; color: var(--ink);
    font-size: 30px; line-height: 1.05;
  }
  .brand-name small { display: block; font-size: 22px; font-weight: 500; }
  .flag-row {
    width: 210px; height: 14px;
    background: linear-gradient(90deg, #b22234, #ffffff 12%, #d52b1e 22%, #006847 32%, #012169 42%, #ffffff 50%, #0055a4 60%, #009246 70%, #ce1126 78%, #000 84%, #00247d 92%, #007a4d);
  }
  /* Back */
  .card-back { top: 514px; background: var(--paper); }
  .back-bands { position: absolute; inset: 0; }
  .back-brand { position: absolute; left: 34px; top: 34px; }
  .back-brand .brand-dot { width: 46px; height: 46px; }
  .back-brand .brand-name { font-size: 23px; }
  .back-brand .brand-name small { font-size: 17px; }
  .back-flags { position: absolute; right: 34px; top: 56px; }
  .contact {
    position: absolute; left: 34px; bottom: 20px; right: 34px;
    color: var(--white);
  }
  .person { font-size: 21px; font-weight: 700; margin-bottom: 6px; }
  .person .role { font-weight: 400; font-size: 15px; }
  .company { font-size: 15px; font-weight: 700; margin-bottom: 4px; }
  .line { font-size: 13px; display: flex; align-items: center; gap: 6px; margin-bottom: 4px; }
  .line-row { display: flex; gap: 20px; }
  .icon { width: 11px; height: 11px; fill: var(--white); flex: none; }
</style>
</head>
<body>

<section class="card card-front" aria-label="Business card front">
  <div class="frame-navy">
    <div class="frame-gold">
      <div class="front-field">
        <div class="brand">
          <span class="brand-dot"></span>
          <p class="brand-name">Tavrelis Global<small>Advisors, LLC</small></p>
        </div>
        <div class="flag-row" role="img" aria-label="Row of small country flags"></div>
      </div>
    </div>
  </div>
</section>

<section class="card card-back" aria-label="Business card back">
  <svg class="back-bands" viewBox="0 0 620 354" preserveAspectRatio="none" aria-hidden="true">
    <path d="M0,148 Q300,205 620,158 L620,354 L0,354Z" fill="var(--lime)"/>
    <path d="M0,165 Q300,222 620,188 L620,354 L0,354Z" fill="var(--red)"/>
    <path d="M0,182 Q300,238 620,210 L620,354 L0,354Z" fill="var(--navy)"/>
  </svg>

  <div class="brand back-brand">
    <span class="brand-dot"></span>
    <p class="brand-name">Tavrelis Global<small>Advisors, LLC</small></p>
  </div>
  <div class="flag-row back-flags" role="img" aria-label="Row of small country flags"></div>

  <div class="contact">
    <p class="person">Dorothy Tavrelis | <span class="role">President</span></p>
    <p class="company">Tavrelis Global Advisors, LLC</p>
    <p class="line">
      <svg class="icon" viewBox="0 0 12 12"><path d="M6 1 L11 6 H9.5 V11 H7 V8 H5 V11 H2.5 V6 H1Z"/></svg>
      7 Birchwood Lane, Milford, VT 05712
    </p>
    <div class="line-row">
      <p class="line">
        <svg class="icon" viewBox="0 0 12 12"><path d="M1 4 Q6 0 11 4 L9 6 L7.5 4.5 H4.5 L3 6Z M3 7 H9 V11 H3Z"/></svg>
        603-555-0148
      </p>
      <p class="line">
        <svg class="icon" viewBox="0 0 12 12"><path d="M1 3 H11 V10 H1Z" fill="none" stroke="#fff" stroke-width="1.2"/><path d="M1 3 L6 7 L11 3" fill="none" stroke="#fff" stroke-width="1.2"/></svg>
        dorot@tavrelis.com
      </p>
      <p class="line">
        <svg class="icon" viewBox="0 0 12 12"><path d="M5 7 L7 5 M4 5 L2.5 6.5 a2 2 0 0 0 3 3 L7 8 M8 7 L9.5 5.5 a2 2 0 0 0 -3 -3 L5 4" fill="none" stroke="#fff" stroke-width="1.2"/></svg>
        www.tavrelis.com
      </p>
    </div>
  </div>
</section>

</body>
</html>
```